Redesign Home Page

We need a new home page with a white background. Our company provides singing instruction to students world wide, both in person and on line. We're looking for a very clean and open design with maximum white space. The main goal of the page will be to get users to sign up for our mailing list. The current site is www.kelvarsong.com. I think the new page can be a long page (scrolll down is ok), to allow for more white space while still using the text from the current page.
Updates

Project Deadline Extended
Reason: Hello to all Designers, I apologize for not giving feedback this weekend. We went out of town for the Memorial Day holiday and I had no internet. I will be extending the deadline to Thursday. -Marcus

Target Market(s)

Singers of all ages and abilities, especially beginners.

Industry/Entity Type

It Company

Requirements
Must have
• 1. A white background
2. Lots of open space
3. An email sign up form on the top right that reads:
a. “Improve Your Singing Now.
b. Sign up for our Free Video Series: Tone Quest
4. Testimonails: found on https://www.kelvarsong.com/tone-ascent
5. My logo with the piano
6. My photo
7. Learn about our Lessons in:
a. San Francisco
b. Alameda
8. On Line Programs:
a. Tone Ascent
b. Wavlo Lessons

Nice to have
• Link to current student page: http://kelvarsong.com/what-students-say/students2
Pictures of singers
Video box: Use Marcus_Example
Should not have
• See "KelvarSong Redesign" file for more details.

```html
<!DOCTYPE html>
<html lang="en">
<head>
<meta charset="utf-8">
<title>Marcus Avery Vocal Studio</title>
<link rel="stylesheet" href="https://fonts.googleapis.com/css2?family=Oswald:wght@400;500&family=Roboto:wght@300;400;500&display=swap">
<style>
  :root {
    --brand: #29abe2;
    --brand-dark: #1f8fc4;
    --ink: #222;
    --muted: #555;
    --line: #e1e4e8;
    --panel: #f7f9fb;
    --white: #fff;
  }
  * { box-sizing: border-box; margin: 0; padding: 0; }
  html, body { width: 1200px; height: 1000px; overflow: hidden; background: var(--white); }
  body { position: relative; font-family: "Roboto", Arial, sans-serif; color: var(--ink); }

  .brand { position: absolute; left: 131px; top: 72px; display: flex; align-items: center; gap: 10px; }
  .brand-mark { width: 40px; height: 40px; border: 3px solid var(--brand); border-radius: 50%; }
  .brand-name { font-size: 22px; font-weight: 500; color: #444; }

  .account { position: absolute; right: 130px; top: 96px; display: flex; gap: 16px; font-size: 15px; color: var(--brand); }
  .account span::after { content: ""; display: inline-block; margin-left: 3px; border: 5px solid transparent; border-top: 6px solid #7cc7ea; vertical-align: -3px; }

  .main-nav { position: absolute; left: 131px; top: 126px; width: 941px; height: 51px; background: var(--brand);
    box-shadow: 0 4px 8px rgba(0,0,0,.18); display: flex; align-items: center; padding-left: 19px; }
  .main-nav a { font-family: "Oswald", Arial, sans-serif; font-weight: 400; color: var(--white); text-decoration: none; font-size: 16px; margin-right: 20px; text-transform: uppercase; letter-spacing: -0.2px; }
  .search { position: absolute; right: 16px; top: 16px; display: flex; align-items: flex-end; gap: 6px; }
  .search-field { width: 176px; height: 20px; border-bottom: 1px solid rgba(255,255,255,.7); }
  .search-btn { width: 22px; height: 22px; border: 1px solid rgba(255,255,255,.8); display: flex; align-items: center; justify-content: center; }

  .hero { position: absolute; left: 131px; top: 203px; width: 941px; height: 404px; overflow: hidden;
    background: linear-gradient(90deg, #c9c2b8 0%, #8c8781 40%, #b98f78 65%, #3a2a24 100%); }
  .hero-photo { position: absolute; left: 0; top: 0; width: 100%; height: 100%; }
  .coach-photo { position: absolute; left: 0; top: 20px; width: 340px; height: 384px;
    background: linear-gradient(180deg, #a08776 0%, #2f333a 55%, #22262c 100%); opacity: .9; }
  .coach-caption { position: absolute; left: 11px; top: 314px; width: 272px; }
  .coach-name { font-size: 22px; color: var(--brand); font-weight: 400; }
  .coach-bio { font-size: 14.5px; color: var(--white); line-height: 18px; margin-top: 3px; }

  .signup-title { position: absolute; right: 22px; top: 12px; font-size: 17px; font-weight: 500; color: var(--white); }
  .signup { position: absolute; left: 675px; top: 42px; width: 251px; height: 197px; background: rgba(255,255,255,.2);
    border-radius: 4px; padding: 12px; }
  .signup p { text-align: center; color: var(--white); font-size: 14px; line-height: 18px; margin-bottom: 10px; }
  .field { height: 28px; margin-bottom: 9px; background: linear-gradient(#f3f3f3, #fff); border: 1px solid #ddd;
    font-size: 11px; color: #999; padding: 8px 7px 0; }
  .btn-start { position: absolute; right: 8px; bottom: 7px; background: var(--brand); color: var(--white);
    font-size: 9.5px; padding: 5px 8px; }

  .section-title { position: absolute; top: 638px; font-family: "Oswald", Arial, sans-serif; font-weight: 400; font-size: 19px; color: var(--brand); text-transform: uppercase; letter-spacing: -0.2px; }
  .how-title { left: 131px; }
  .say-title { right: 129px; }

  .how-card { position: absolute; left: 130px; top: 678px; width: 553px; height: 289px; border: 1px solid var(--line); background: var(--panel); }
  .singer-photo { position: absolute; left: 7px; top: 8px; width: 313px; height: 273px;
    background: linear-gradient(135deg, #f4f1ee 0%, #c9a38d 45%, #3b2a26 75%, #e6e4e2 100%); }
  .how-text { position: absolute; left: 327px; top: 8px; width: 218px; font-size: 11px; line-height: 13.5px; color: var(--ink); }
  .how-text p + p { margin-top: 13px; }
  .read-more { display: block; margin-top: 11px; color: var(--brand); font-size: 11px; text-decoration: none; }

  .quote { position: absolute; left: 745px; width: 324px; height: 92px; border: 1px solid var(--line); background: var(--panel); }
  .quote-avatar { position: absolute; left: -32px; top: 8px; width: 72px; height: 72px; border-radius: 50%;
    border: 4px solid var(--white); box-shadow: 0 0 0 1px var(--line); }
  .quote-text { position: absolute; left: 62px; top: 6px; width: 244px; font-size: 11px; line-height: 13.4px; color: var(--ink); }
  .quote-author { display: block; font-family: "Oswald", Arial, sans-serif; font-size: 11.5px; color: var(--brand); margin-top: 1px; }
</style>
</head>
<body>
  <header>
    <div class="brand"><span class="brand-mark"></span><span class="brand-name">Marcus Avery</span></div>
    <div class="account"><span>Sign up</span><span>Log in</span></div>
    <nav class="main-nav">
      <a href="#">Home</a><a href="#">Voice Lesson</a><a href="#">Blog</a><a href="#">What Student Say</a><a href="#">Meet the Instructors</a><a href="#">Tone Ascent</a>
      <div class="search">
        <div class="search-field"></div>
        <div class="search-btn">
          <svg width="12" height="12" viewBox="0 0 12 12"><circle cx="5" cy="5" r="3.6" fill="none" stroke="#fff" stroke-width="1.6"/><line x1="7.6" y1="7.6" x2="11" y2="11" stroke="#fff" stroke-width="1.8"/></svg>
        </div>
      </div>
    </nav>
  </header>

  <section class="hero">
    <div class="hero-photo" role="img" aria-label="Blurred studio photo of a woman singing into a microphone"></div>
    <div class="coach-photo" role="img" aria-label="Portrait of vocal coach Marcus Avery in a dark turtleneck"></div>
    <div class="coach-caption">
      <h2 class="coach-name">Marcus Avery</h2>
      <p class="coach-bio">Professional Vocal Coach, Has laid the vocal foundation for thousands of singers worlwide,for 20+ years.</p>
    </div>
    <h1 class="signup-title">IMPROVE YOUR SINGING NOW</h1>
    <form class="signup">
      <p>Sign up for free Video Series<br>Tone Quest</p>
      <div class="field">First Name</div>
      <div class="field">Last Name</div>
      <div class="field">Email</div>
      <span class="btn-start">GET STARTED</span>
    </form>
  </section>

  <h2 class="section-title how-title">How Voice Transformation Works</h2>
  <h2 class="section-title say-title">What Students Say ?</h2>

  <article class="how-card">
    <div class="singer-photo" role="img" aria-label="Woman with headphones singing joyfully at a studio microphone"></div>
    <div class="how-text">
      <p>After many years of work, I've decided that the effective transformation of the human voice is my life's work and passion. While on line methods of instruction are not a as effective as in person lessons, I find that getting a foundational understanding of the voice that comes with Tone Ascent can greatly enhance your singing voice, whether you're currently studying with a teacher or working on your own.</p>
      <p>From my background as a scientist as well as a musician, I know the potential of the human voice. More importantly, I understand the specific vocal techniques that can unleash brilliance, ease, and power in anyone's singing. (Including yours.)</p>
      <a class="read-more" href="#">read more</a>
    </div>
  </article>

  <blockquote class="quote" style="top:678px">
    <div class="quote-avatar" role="img" aria-label="Student portrait" style="background:linear-gradient(#e8c9b0,#c48d6e)"></div>
    <p class="quote-text">“I am so happy to have met you! Before Tone Ascent, I had vocal problems that clouded my mind and made it zero fun to sing. Now I sing again and even have a weekly job as a speaker.”<span class="quote-author">Anselm, Germany</span></p>
  </blockquote>
  <blockquote class="quote" style="top:775px">
    <div class="quote-avatar" role="img" aria-label="Student portrait" style="background:linear-gradient(#6d8a6a,#3c3128)"></div>
    <p class="quote-text">“Since starting the program, my singing progress has been described as phenomenal, 400% improvement. My teachers have worked with peoplesuch as Dame Elspeth Marlowe, and they are impressed with my voice.”<span class="quote-author">Declan Hurley , Australia</span></p>
  </blockquote>
  <blockquote class="quote" style="top:873px">
    <div class="quote-avatar" role="img" aria-label="Student portrait" style="background:linear-gradient(#8a6a50,#1e1a18)"></div>
    <p class="quote-text">“I have found through the years that the one method I can count on is Tone Ascent. Marcus Avery has put together the fool proof method for training a voice that is dependable and authentic as you grow through your vocal.”<span class="quote-author">Corinne Wald, San Francisco</span></p>
  </blockquote>
</body>
</html>
```